Spa needs a highly desired Membership Card

We need a membership card that captures people's desire to own it(our membership) when flashed by anyone! It should tell the "class" of the card owner!
Comes in Silver & Gold membership. Wants to have same design in different colour/tone to differentiate Gold & Silver.
Most members are woman, but we have few men as well.
Updates
Hi Designers,
Target Market(s)
Woman age 25-55 years old. High spending power in a relatively poor country(Myanmar).
They may be rich businesswomen, wives/daughters of rich man, women who are educated abroad and now return to home country as Myanmar is fast developing.
Requirements
Must have
- Must be in tiff, bmp or jpeg format so that card printer can recognise.
- TEXT
- Velmora Spa (font: Monotype Corsiva)
- No 18, Kethin Street, Sula Court (Level-2) (4117), Dagon Township, Yangon
- 09 47268031
- contactus@ternwick-holdco.example
- A space for picture of card owner.
- No magnetic strip/smart chip.
- Name Abcdefghijklmn
- Membership No 12345678
- Expiry MM/YYYY
- For Gold:
- Terms and Conditions
- - Members enjoy 25% off all standard services, excluding promotional offers
- - Members enjoy 5% off for Quessaline products, excluding promotional items
- - Members enjoy 10% off for all other retail products, excluding promotional items
- - 1 accompanying guest in a day enjoys 20% off standard services, excluding promotional offers
- - Memberships are valid for 2 years from the date of issue and are non-transferable
- - Memberships sold are non-refundable or exchangeable for cash, services or products
- - Privileges are subject to change without prior notice
- For Silver:
- Terms and Conditions
- - Members enjoy 20% off all standard services, excluding promotional offers
- I uploaded 2 of our spa pictures so you can have a feel our of premise. And uploaded our name card, I agree its not stylish as I designed it myself.

```html
<!DOCTYPE html>
<html lang="en">
<head>
<meta charset="utf-8">
<title>Velmora Spa – Gold Membership Card</title>
<link rel="stylesheet" href="https://fonts.googleapis.com/css2?family=Italianno&family=Open+Sans:wght@400;600&display=swap">
<style>
  :root {
    --canvas: #ecebe6;
    --card-light: #eef0b4;
    --card-mid: #dfe29a;
    --band-dark: #5a521c;
    --band-mid: #7d7229;
    --ink: #6b6326;
    --ink-soft: #8a8240;
    --on-band: #e9e6a8;
    --ornament: #cfd08a;
  }
  * { margin: 0; padding: 0; box-sizing: border-box; }
  html, body { width: 1200px; height: 724px; overflow: hidden; }
  body {
    background: var(--canvas);
    font-family: "Open Sans", Arial, sans-serif;
    color: var(--ink);
    position: relative;
  }
  .card {
    position: absolute;
    top: 192px;
    width: 540px;
    height: 340px;
    border-radius: 6px;
    overflow: hidden;
    background: linear-gradient(135deg, var(--card-light), var(--card-mid));
    box-shadow: 0 6px 18px rgba(0,0,0,0.18);
  }
  .card--front { left: 40px; }
  .card--back { left: 620px; }

  /* Front */
  .band { position: absolute; inset: 0; }
  .ornament-top {
    position: absolute;
    top: 0; left: 300px;
    width: 170px; height: 70px;
    border-radius: 0 0 60px 60px;
    background: radial-gradient(ellipse at center, var(--ornament), transparent 72%);
  }
  .member {
    position: absolute;
    left: 210px; top: 74px;
    font-size: 13px;
    line-height: 1.45;
  }
  .member__name { font-weight: 600; margin-bottom: 4px; }
  .photo-box {
    position: absolute;
    left: 56px; top: 130px;
    width: 140px; height: 130px;
    border: 1px solid var(--ink-soft);
  }
  .brand {
    position: absolute;
    display: flex;
    align-items: center;
    gap: 8px;
    font-family: "Open Sans", Arial, sans-serif;
    font-weight: 600;
  }
  .brand__dot {
    width: 18px; height: 18px;
    border-radius: 50%;
    border: 1.5px solid currentColor;
  }
  .card--front .brand {
    right: 22px; top: 74px;
    color: var(--on-band);
    font-size: 15px;
  }

  /* Back */
  .card--back .brand {
    left: 40px; top: 150px;
    flex-direction: column;
    font-size: 18px;
    color: var(--ink);
  }
  .card--back .brand__dot { width: 44px; height: 44px; }
  .ornament-corner {
    position: absolute;
    top: 12px; right: 16px;
    width: 56px; height: 40px;
    border-radius: 50%;
    background: radial-gradient(ellipse at center, var(--ornament), transparent 70%);
  }
  .contact {
    position: absolute;
    left: 230px; top: 44px;
    width: 280px;
    font-size: 11px;
    line-height: 1.5;
  }
  .contact__name { font-weight: 600; font-size: 12px; }
  .contact__rule { height: 1px; background: var(--ink-soft); margin: 8px 0; width: 200px; }
  .contact__line { display: flex; align-items: center; gap: 6px; }
  .contact__line svg { width: 10px; height: 10px; fill: var(--ink); flex: none; }
  .terms {
    margin-top: 12px;
    font-size: 8.5px;
    line-height: 1.55;
    color: var(--ink-soft);
  }
  .terms__title { font-weight: 600; color: var(--ink); font-size: 9px; margin-bottom: 2px; }
</style>
</head>
<body>

<section class="card card--front" aria-label="Gold membership card front">
  <svg class="band" viewBox="0 0 540 340" aria-hidden="true">
    <defs>
      <linearGradient id="bandFill" x1="0" y1="0" x2="1" y2="1">
        <stop offset="0" stop-color="#7d7229"/>
        <stop offset="1" stop-color="#514a17"/>
      </linearGradient>
      <path id="bandCurve" d="M250 330 C330 250 360 200 420 120 C450 80 480 40 520 10"/>
    </defs>
    <path d="M430 0 C400 90 330 150 300 210 C275 260 240 300 215 340 L540 340 L540 0 Z" fill="url(#bandFill)"/>
    <path d="M440 0 C412 92 345 152 315 212 C290 262 258 302 235 340" fill="none" stroke="#e9e6a8" stroke-width="1.2" opacity="0.8"/>
    <path d="M422 0 C392 88 322 148 292 208 C268 258 232 298 206 340" fill="none" stroke="#7d7229" stroke-width="2"/>
    <text font-family="Italianno, cursive" font-size="34" fill="#e9e6a8">
      <textPath href="#bandCurve" startOffset="6%">Gold Membership</textPath>
    </text>
  </svg>
  <div class="ornament-top" role="img" aria-label="Decorative flourish ornament"></div>
  <div class="brand"><span class="brand__dot"></span>Velmora Spa</div>
  <div class="member">
    <p class="member__name">Mr. John Doe</p>
    <p>ID# XXX-XXXX-XX</p>
    <p>(000) 000000000</p>
    <p>(00) 00000000</p>
  </div>
  <div class="photo-box" aria-label="Space for member photo"></div>
</section>

<section class="card card--back" aria-label="Gold membership card back">
  <div class="ornament-corner" role="img" aria-label="Small flourish ornament"></div>
  <div class="brand"><span class="brand__dot"></span>Velmora Spa</div>
  <div class="contact">
    <p class="contact__name">Aron Thet Min</p>
    <p>Director</p>
    <p>(959) 452203861 (YGN)</p>
    <p>(65) 91736245 (SGP)</p>
    <div class="contact__rule"></div>
    <p>No 18, Kethin Street, Sula Court (Level-2) (4117),<br>Dagon Township, Yangon</p>
    <p class="contact__line"><svg viewBox="0 0 10 10"><path d="M2 0h2l1 3-1.5 1a6 6 0 0 0 2.5 2.5L7 5l3 1v2a2 2 0 0 1-2 2A8 8 0 0 1 0 2a2 2 0 0 1 2-2z"/></svg>09 47268031</p>
    <p>contactus@ternwick-holdco.example</p>
    <div class="terms">
      <p class="terms__title">TERMS &amp; CONDITIONS</p>
      <p>Members enjoy 25% off standard services.</p>
      <p>Members enjoy 5% off Quessaline products.</p>
      <p>Guest enjoys 20% off standard services.</p>
      <p>Valid two years, non-transferable.</p>
      <p>Non-refundable; privileges may change.</p>
    </div>
  </div>
</section>

</body>
</html>
```